Amber Ridge Publishing Web Page Design

Design a website for my new start up publishing company - Amber Ridge Publishing, the first work published by ARP with be a new book by M.R. Theodor called Silent Ledger. The prototype for the book cover is attached.

Target Market(s)

Worldwide, all readers of mystery, fiction, etc.

Industry/Entity Type

Book Publisher

Coding

Coded - Design and coding required

Number of Pages Required

1 page

```html
<!DOCTYPE html>
<html lang="en">
<head>
<meta charset="utf-8">
<title>Amber Ridge Publishing — Bookshop</title>
<link rel="stylesheet" href="https://fonts.googleapis.com/css2?family=Raleway:wght@300;500;600;700&display=swap">
<style>
  :root {
    --ink-dark: #17130f;
    --hero-shadow: #241c16;
    --hero-mist: #5d554e;
    --white: #ffffff;
    --gold: #ac8b54;
    --gold-light: #c7a76c;
    --button-grey: rgba(150, 146, 142, 0.72);
    --indicator-dim: rgba(110, 104, 98, 0.85);
    --cover-deep: #171c3f;
    --cover-mid: #2c3a78;
    --cover-glow: #6b76b8;
    --card-teal: #2c4650;
    --card-warm: #8c6c52;
    --page-bg: #ffffff;
  }
  * { box-sizing: border-box; margin: 0; padding: 0; }
  html, body {
    width: 1200px; height: 2402px; overflow: hidden;
    background: var(--page-bg);
    font-family: "Raleway", Arial, sans-serif;
  }
  .page { position: relative; width: 1200px; height: 2402px; overflow: hidden; }

  /* Hero */
  .hero {
    position: absolute; left: 0; top: 0; width: 1200px; height: 1060px;
    background:
      radial-gradient(ellipse 420px 520px at 330px 480px, rgba(140,130,120,0.55), transparent 70%),
      linear-gradient(180deg, var(--ink-dark) 0%, var(--hero-shadow) 55%, var(--hero-mist) 100%);
    overflow: hidden;
  }
  .hero-cover {
    position: absolute; left: 600px; top: 0; width: 600px; height: 1060px;
    background:
      radial-gradient(ellipse 160px 420px at 420px 700px, var(--cover-glow), transparent 75%),
      linear-gradient(160deg, var(--cover-mid) 0%, var(--cover-deep) 100%);
    box-shadow: -18px 0 40px rgba(0,0,0,0.5);
  }
  .brand {
    position: absolute; left: 96px; top: 146px;
    color: var(--white); font-weight: 600; font-size: 46px; line-height: 52px;
  }
  .menu-toggle { position: absolute; left: 1063px; top: 190px; }
  .book-title {
    position: absolute; left: 96px; top: 500px;
    color: var(--white); font-weight: 700; font-size: 74px; letter-spacing: 1px;
  }
  .book-author {
    position: absolute; left: 100px; top: 630px;
    color: var(--white); font-weight: 700; font-size: 52px;
  }
  .buy-button {
    position: absolute; left: 98px; top: 746px; width: 316px; height: 102px;
    background: var(--button-grey); color: var(--white);
    font-weight: 600; font-size: 36px; letter-spacing: 1px;
    display: flex; align-items: center; justify-content: center;
  }
  .wishlist-tag {
    position: absolute; left: 1108px; top: 592px; width: 92px; height: 76px;
    background: var(--gold);
    display: flex; align-items: center; justify-content: center;
  }
  .slide-indicators {
    position: absolute; left: 363px; top: 1018px; display: flex; gap: 12px;
  }
  .slide-indicators span { width: 108px; height: 12px; background: var(--indicator-dim); }
  .slide-indicators span.active { background: var(--white); }

  /* Welcome */
  .welcome {
    position: absolute; left: 0; top: 1060px; width: 1200px; height: 808px;
    background: var(--gold); color: var(--white);
  }
  .welcome-heading {
    position: absolute; left: 98px; top: 130px;
    font-weight: 700; font-size: 40px; line-height: 56px; letter-spacing: 3px;
  }
  .bag-button {
    position: absolute; left: 1058px; top: 88px; width: 104px; height: 104px;
    border-radius: 50%; background: var(--gold-light);
    display: flex; align-items: center; justify-content: center;
  }
  .welcome-text {
    position: absolute; left: 98px; top: 278px; width: 1060px;
    font-weight: 600; font-size: 40px; line-height: 56px;
  }
  .anniversary {
    position: absolute; left: 495px; top: 570px; width: 210px; height: 210px;
    border-radius: 50%;
    background: radial-gradient(circle, rgba(255,255,255,0.14) 55%, rgba(255,255,255,0.32) 56%, rgba(255,255,255,0.32) 62%, transparent 63%);
    display: flex; flex-direction: column; align-items: center; justify-content: center;
    color: var(--white); text-align: center;
  }
  .anniversary-number { font-weight: 700; font-size: 60px; line-height: 56px; }
  .anniversary-years { font-weight: 500; font-size: 36px; line-height: 38px; }
  .anniversary-label { font-weight: 500; font-size: 18px; letter-spacing: 1px; }

  /* Feature card */
  .feature-card {
    position: absolute; left: 98px; top: 1924px; width: 1126px; height: 478px;
    left: 37px;
    background:
      radial-gradient(ellipse 300px 260px at 560px 380px, var(--card-warm), transparent 75%),
      linear-gradient(180deg, #34505a 0%, var(--card-teal) 100%);
    overflow: hidden;
  }
  .feature-heading {
    position: absolute; left: 36px; top: 48px;
    color: var(--white); font-weight: 300; font-size: 66px; line-height: 78px;
  }
</style>
</head>
<body>
<main class="page">

  <section class="hero">
    <div class="hero-backdrop" role="img" aria-label="Misty night scene with a figure standing on dark ground"></div>
    <div class="hero-cover" role="img" aria-label="Silent Ledger book cover in blue with a lightning strike"></div>

    <div class="brand">Amber Ridge<br>Publishing</div>

    <svg class="menu-toggle" width="96" height="48" viewBox="0 0 96 48" aria-label="Menu">
      <rect x="0" y="0" width="96" height="7" fill="#ffffff"/>
      <rect x="0" y="20" width="96" height="7" fill="#ffffff"/>
      <rect x="0" y="40" width="96" height="7" fill="#ffffff"/>
    </svg>

    <h1 class="book-title">SILENT LEDGER</h1>
    <p class="book-author">M.R. THEODOR</p>
    <div class="buy-button">BUY NOW</div>

    <div class="wishlist-tag">
      <svg width="50" height="44" viewBox="0 0 24 22" aria-label="Add to wishlist">
        <path d="M12 21 L2.5 11.5 A5.5 5.5 0 0 1 12 4 A5.5 5.5 0 0 1 21.5 11.5 Z" fill="#ffffff"/>
      </svg>
    </div>

    <div class="slide-indicators">
      <span class="active"></span><span></span><span></span><span></span>
    </div>
  </section>

  <section class="welcome">
    <h2 class="welcome-heading">WELCOME TO THE BOOKSHOP AND<br>THANKS FOR VISITING US.</h2>

    <div class="bag-button">
      <svg width="52" height="56" viewBox="0 0 26 28" aria-label="Shopping bag">
        <path d="M3 9 H23 L21.5 26 H4.5 Z" fill="none" stroke="#ffffff" stroke-width="2"/>
        <path d="M8.5 11 V6 A4.5 4.5 0 0 1 17.5 6 V11" fill="none" stroke="#ffffff" stroke-width="2"/>
        <path d="M13 22 L9.5 18.5 A2 2 0 0 1 13 16 A2 2 0 0 1 16.5 18.5 Z" fill="#ffffff"/>
      </svg>
    </div>

    <p class="welcome-text">Amber Ridge Publishing, is a leading independent publishing house established in 1999.<br>Free shipping on all UK orders, earn reward points, build wishlists, redeem your gift cards.</p>

    <div class="anniversary" role="img" aria-label="Laurel wreath anniversary emblem">
      <span class="anniversary-number">20</span>
      <span class="anniversary-years">YEARS</span>
      <span class="anniversary-label">ANNIVERSARY</span>
    </div>
  </section>

  <section class="feature-card" role="img" aria-label="Person holding a lit sparkler against a dusky blue background">
    <h2 class="feature-heading">CELEBRATING OF<br>INDEPENDENT<br>PUBLISHING</h2>
  </section>

</main>
</body>
</html>
```